Steady Harbor Claims Group Business card

Need a business card that stands out that includes name of company,(above) Owners name Moira Lindqvist phone#517-362-4408 email# SteadyHarborCG@mailvane.com and website www.Steadyharborclaimsgroup.net. This is a medical billing company so the card has to relate to that or relate to increasing revenue

```html
<!DOCTYPE html>
<html lang="en">
<head>
<meta charset="utf-8">
<title>Steady Harbor Claims Group – Business Card</title>
<link rel="stylesheet" href="https://fonts.googleapis.com/css2?family=Open+Sans:wght@400;600;700&display=swap">
<style>
  :root {
    --page-bg: #ecebe8;
    --card-bg: #ffffff;
    --brand-blue: #2b7ba8;
    --band-blue: #2f7fa7;
    --brand-green: #8cc63f;
    --text-body: #4a4a4a;
    --rule: #d9dee2;
  }
  * { box-sizing: border-box; margin: 0; padding: 0; }
  html, body {
    width: 1200px; height: 1000px; overflow: hidden;
    background: var(--page-bg);
    font-family: "Open Sans", Arial, sans-serif;
  }
  .canvas { position: relative; width: 1200px; height: 1000px; }
  .card {
    position: absolute; left: 265px; width: 666px; height: 398px;
    background: var(--card-bg);
    box-shadow: 0 4px 10px rgba(0,0,0,0.18);
    overflow: hidden;
  }
  .card--front { top: 73px; }
  .card--back { top: 532px; }

  .brand {
    position: absolute; left: 32px; top: 140px;
    display: flex; align-items: center; gap: 12px;
  }
  .brand__mark { width: 22px; height: 22px; background: var(--brand-blue); }
  .brand__name {
    font-size: 24px; font-weight: 600; color: var(--brand-blue);
    letter-spacing: 0.5px;
  }

  .divider {
    position: absolute; left: 32px; top: 246px; width: 408px; height: 1px;
    background: var(--rule);
  }
  .owner-name {
    position: absolute; right: 32px; top: 235px;
    font-size: 20px; font-weight: 700; color: var(--brand-blue);
    letter-spacing: 0.3px;
  }

  .contact { position: absolute; left: 32px; top: 270px; list-style: none; }
  .contact__item {
    display: flex; align-items: center; gap: 8px;
    height: 26px; font-size: 16px; color: var(--text-body);
  }
  .contact__icon { width: 15px; height: 15px; fill: var(--brand-blue); flex: none; }

  .band { position: absolute; left: 0; bottom: 0; width: 666px; height: 40px; }

  .services { position: absolute; left: 33px; top: 66px; }
  .services__title {
    font-size: 16px; font-weight: 600; color: var(--brand-blue); margin-bottom: 8px;
  }
  .services__list { list-style: none; }
  .services__item {
    position: relative; padding-left: 12px;
    height: 26px; line-height: 26px;
    font-size: 16px; color: var(--text-body);
  }
  .services__item::before {
    content: ""; position: absolute; left: 0; top: 11px;
    width: 5px; height: 5px; border-radius: 50%; background: var(--brand-blue);
  }
</style>
</head>
<body>
<main class="canvas">

  <section class="card card--front" aria-label="Business card front">
    <div class="brand">
      <span class="brand__mark"></span>
      <span class="brand__name">Steady Harbor Claims Group</span>
    </div>

    <div class="divider"></div>
    <h1 class="owner-name">MOIRA LINDQVIST</h1>

    <ul class="contact">
      <li class="contact__item">
        <svg class="contact__icon" viewBox="0 0 16 16" aria-hidden="true"><path d="M2 5c0-2 2-3 6-3s6 1 6 3v1h-3V5H5v1H2z M4 7h8l2 6H2z"/></svg>
        517-362-4408
      </li>
      <li class="contact__item">
        <svg class="contact__icon" viewBox="0 0 16 16" aria-hidden="true"><path d="M1 3h14v10H1z" fill="var(--brand-blue)"/><path d="M1.5 3.5 8 9l6.5-5.5" fill="none" stroke="#fff" stroke-width="1.3"/></svg>
        SteadyHarborCG@mailvane.com
      </li>
      <li class="contact__item">
        <svg class="contact__icon" viewBox="0 0 16 16" aria-hidden="true"><circle cx="8" cy="8" r="6.5" fill="none" stroke="var(--brand-blue)" stroke-width="1.6"/><path d="M1.5 8h13M8 1.5c-3 3-3 10 0 13M8 1.5c3 3 3 10 0 13" fill="none" stroke="var(--brand-blue)" stroke-width="1.2"/></svg>
        Steadyharborclaimsgroup.net
      </li>
    </ul>

    <svg class="band" viewBox="0 0 666 40" preserveAspectRatio="none" aria-hidden="true">
      <path d="M0 9 H330 C350 9 352 18 346 20 H0 Z" fill="var(--brand-green)"/>
      <path d="M330 40 C345 18 355 2 395 2 H666 V40 Z" fill="var(--band-blue)"/>
      <path d="M0 20 H322 C340 20 350 6 395 0" fill="none" stroke="#fff" stroke-width="2.5"/>
      <path d="M0 22 H666 V40 H0 Z" fill="var(--band-blue)"/>
    </svg>
  </section>

  <section class="card card--back" aria-label="Business card back">
    <div class="services">
      <h2 class="services__title">Steady Harbor Claims Group Services</h2>
      <ul class="services__list">
        <li class="services__item">Account Receivable Audits &amp; Collections</li>
        <li class="services__item">Aggressive Insurance Collection</li>
        <li class="services__item">Claims Follow-Up</li>
        <li class="services__item">Coding</li>
        <li class="services__item">Detailed Monthly Reports</li>
        <li class="services__item">Electronic Claims Resubmissions</li>
        <li class="services__item">Evaluation and Review of Billing Structure</li>
        <li class="services__item">Patient Billing &amp; Collections</li>
        <li class="services__item">Payment Posting</li>
      </ul>
    </div>
  </section>

</main>
</body>
</html>
```